Book Cover Design for first time business owners

Looking for a design for my book, 'LAYING THE GROUNDWORK' subtitle is
THE REAL ESTATE, DESIGN, & CONSTRUCTION STEPS TO OPENING YOUR RETAIL OR FOOD-SERVICE CONCEPT ON-TIME AND ON BUDGET

If it helps, below is part of the preface:

These pages derive from my experiences and industry standards. This book runs through the budgeting, real estate, design, construction, signage, and equipment processes needed to get any retail or restaurant space open on-time and on budget while saving you time, money, and headaches along the way.

Whether it be a one-off enterprise or franchise, flower shop, or swim center; the steps and procedures are strikingly similar. Whether you’re looking to spend $200,000 or $2,000,000, it’s all largely the same.
This book does not discuss marketing or operations as those items are more concept specific, and outside the confines of this book.
Technically food-service concepts (restaurants, cafés, and bars) are not considered retail. For the basis of this book and to streamline writing, mentions of retail include food-service concepts.

Target Market(s)

First time business Owners looking to construct a retail or food-service concept

Font styles to use
Serif

Requirements
Must have
• I'm open to any designs! Looking for the design to wrap around the front, spine, and back.
• Please include the authors name on the front: Corwin Halbeck. The Authors name size should not be overly intrusive.
• I'm still working on the verbiage for the back of the book. That verbiage will be on the top half of the back.

```html
<!DOCTYPE html>
<html lang="en">
<head>
<meta charset="utf-8">
<title>Laying the Groundwork — Corwin Halbeck</title>
<link rel="stylesheet" href="https://fonts.googleapis.com/css2?family=Montserrat:wght@300;400;800&family=Open+Sans:wght@400&display=swap">
<style>
  :root {
    --paper: #ffffff;
    --ink: #454440;
    --ink-soft: #2f2f2f;
    --blue: #1e8fff;
    --yellow: #ffd200;
    --red: #ff3b2b;
  }
  html, body {
    margin: 0;
    padding: 0;
    overflow: hidden;
    background: var(--paper);
  }
  .cover {
    position: relative;
    width: 800px;
    height: 1200px;
    background: var(--paper);
    overflow: hidden;
    color: var(--ink);
  }
  .title {
    position: absolute;
    top: 160px;
    left: 0;
    width: 100%;
    margin: 0;
    text-align: center;
    font-weight: normal;
  }
  .title-lead {
    display: block;
    font-family: "Montserrat", sans-serif;
    font-weight: 300;
    font-size: 68px;
    line-height: 74px;
    letter-spacing: 6px;
  }
  .title-main {
    display: block;
    margin-top: 20px;
    font-family: "Montserrat", sans-serif;
    font-weight: 800;
    font-size: 92px;
    line-height: 100px;
    letter-spacing: 1px;
  }
  .cover-art {
    position: absolute;
    left: 288px;
    top: 376px;
    width: 224px;
    height: 470px;
    border-radius: 8px;
    background: linear-gradient(90deg, var(--blue) 0%, var(--yellow) 50%, var(--red) 100%);
    opacity: 0.35;
  }
  .subtitle {
    position: absolute;
    top: 888px;
    left: 0;
    width: 100%;
    margin: 0;
    text-align: center;
    font-family: "Open Sans", sans-serif;
    font-size: 17.5px;
    line-height: 30px;
    letter-spacing: 0.3px;
    color: var(--ink-soft);
  }
  .author {
    position: absolute;
    top: 1108px;
    left: 0;
    width: 100%;
    margin: 0;
    text-align: center;
    font-family: "Montserrat", sans-serif;
    font-weight: 400;
    font-size: 40px;
    line-height: 50px;
    letter-spacing: 4px;
    color: #1e1e1e;
  }
</style>
</head>
<body>
  <main class="cover">
    <h1 class="title">
      <span class="title-lead">LAYING THE</span>
      <span class="title-main">GROUNDWORK</span>
    </h1>
    <div class="cover-art" role="img" aria-label="Illustration of a house painted in blue, yellow and red stripes formed by a paint roller with a long handle"></div>
    <p class="subtitle">THE REAL ESTATE, DESIGN, &amp; CONSTRUCTION STEPS TO OPENING<br>YOUR RETAIL OR FOOD-SERVICE CONCEPT ON-TIME AND ON BUDGET</p>
    <p class="author">CORWIN HALBECK</p>
  </main>
</body>
</html>
```